Zorveli Foods Web Page Templates

I need two templates designed for a wholesale food/catering business, one template for the home page and the other for detail pages. The overall template should be a simple, clean and clear design. I have provided the existing logo to which the templates should directly relate.
Zorveli Foods supplies food based upon traditional Ghanian recipes to a number of stores across Canberra. In addition, Zorveli Foods offers catering for public and private functions across the Canberra region.
The colours in the logo represent the national colours of Ghana (yellow, green, red and black) and the website content will also include traditional Ghanian Kente patterns which will add further colour elements to the site. On this basis, the template design needs to be fairly sparse so as not to compete with the colourful content of the website detail pages.
There is no requirement for specific pages to be designed, as these will be handled in the CMS implementation.
The information provided in the Word document is only designed to provide a sense of the intended content of the website, not as a requirement for specific pages to be produced.

Target Market(s)

Retail/Wholesale food

Number of Pages Required

2 page

Font styles to use
Serif

Colors

Designer to choose colors to be used in the design.

Requirements
Must have
• Template must accommodate a responsive design
• The logo provided will form the cornerstone of the design
Nice to have
• There
Should not have
• Please do not solicit for extra work or for alternative logo design.

```html
<!DOCTYPE html>
<html lang="en">
<head>
<meta charset="utf-8">
<title>Zorveli Foods</title>
<link href="https://fonts.googleapis.com/css2?family=Montserrat:wght@400;500;600;700&family=Open+Sans:wght@400;600&display=swap" rel="stylesheet">
<style>
:root{
  --green:#678540;
  --green-dark:#55702f;
  --red:#e0271b;
  --black:#000;
  --ink:#1b1b1b;
  --muted:#8a8a8a;
  --grey-bg:#ececec;
  --white:#fff;
}
*{box-sizing:border-box;margin:0;padding:0}
html,body{width:1200px;height:3586px;overflow:hidden}
body{font-family:"Open Sans",Arial,sans-serif;color:var(--ink);background:var(--white);position:relative}
.head{font-family:"Montserrat",Arial,sans-serif}
section,header,footer{position:relative;width:1200px}
.abs{position:absolute}

/* header */
.site-header{height:84px}
.brand{position:absolute;left:38px;top:26px;display:flex;align-items:center;gap:8px;font-family:"Montserrat",sans-serif;font-weight:700;font-size:19px;color:var(--green)}
.brand-dot{width:12px;height:12px;border-radius:50%;background:var(--red)}
.main-nav{position:absolute;left:208px;top:34px;display:flex;gap:22px;font-family:"Montserrat",sans-serif;font-size:11px;font-weight:600;color:#333}
.main-nav .active{color:var(--green)}
.search-icon{position:absolute;left:862px;top:30px}
.btn-customer{position:absolute;left:893px;top:30px;width:150px;height:22px;border-radius:11px;background:var(--green);color:#fff;font:600 9px "Montserrat",sans-serif;display:flex;align-items:center;justify-content:center}
.btn-order{position:absolute;left:1050px;top:30px;width:112px;height:22px;border-radius:11px;border:1.5px solid var(--green);color:var(--green);font:600 9px "Montserrat",sans-serif;display:flex;align-items:center;justify-content:center}

/* hero */
.hero{height:447px}
.hero-photo{position:absolute;inset:0;background:radial-gradient(ellipse at 62% 55%,#7a3d14 0%,#5a2a0c 35%,#3b1a08 60%,#c8bfb4 90%)}
.hero-card{position:absolute;left:160px;top:119px;width:352px;height:210px;background:#fff;padding:22px 24px}
.hero-card .kicker{font:500 13px "Montserrat",sans-serif}
.hero-card h1{font:700 26px "Montserrat",sans-serif;margin:2px 0 10px}
.hero-card p{font-size:11px;line-height:1.7}
.pill-red{display:inline-flex;align-items:center;justify-content:center;margin-top:12px;width:94px;height:28px;border-radius:14px;background:var(--red);color:#fff;font:600 10px "Montserrat",sans-serif}
.hero-arrow{position:absolute;top:287px;width:38px;height:38px;border-radius:50%;background:#fff;display:flex;align-items:center;justify-content:center}

/* who we service */
.service{height:652px}
.service-title{position:absolute;left:160px;top:60px;font:500 31px/1.15 "Montserrat",sans-serif}
.service-title b{color:var(--red);font-weight:700;display:block}
.service-sub{position:absolute;left:160px;top:155px;width:200px;font-size:10px;line-height:1.6;color:var(--muted)}
.shop-tile{position:absolute;width:200px;height:251px}
.shop-image{height:196px;background:var(--green);display:flex;align-items:center;justify-content:center;color:#fff;font:700 16px "Montserrat",sans-serif}
.shop-name{height:55px;background:var(--red);color:#fff;font:700 11.5px/1.35 "Montserrat",sans-serif;padding:0 10px;display:flex;align-items:center}

/* about */
.about{height:263px;background:var(--black);color:#fff;text-align:center}
.section-title{font:400 28px "Montserrat",sans-serif;text-align:center}
.section-title b{color:var(--red);font-weight:700}
.about .section-title{color:#fff;padding-top:38px;font-size:24px}
.about .section-title b{color:#fff}
.about h3{font:500 14px "Open Sans",sans-serif;margin-top:16px}
.about p{width:880px;margin:16px auto 0;font-size:10.5px;line-height:2.1}

/* casseroles */
.casseroles{height:502px}
.casseroles .section-title{padding-top:48px}
.dish{position:absolute;top:124px;width:280px}
.dish-photo{height:270px}
.dish h4{margin-top:16px;font:700 14px/1.2 "Montserrat",sans-serif}

/* catering band */
.catering{height:127px;background:var(--green)}
.catering p{position:absolute;left:160px;top:36px;width:600px;color:#fff;font:600 15px/1.7 "Montserrat",sans-serif}
.btn-outline-light{position:absolute;left:887px;top:48px;width:153px;height:31px;border-radius:16px;background:#fff;color:var(--green-dark);font:600 10px "Montserrat",sans-serif;display:flex;align-items:center;justify-content:center}

/* offer */
.offer{height:458px}
.offer .section-title{padding-top:54px}
.offer-card{position:absolute;top:126px;width:428px}
.offer-photo{height:208px}
.offer-label{height:60px;background:var(--red);color:#fff;font:700 15px/1.35 "Montserrat",sans-serif;padding:10px 14px}

/* blog */
.blog{height:646px;background:var(--grey-bg)}
.blog .section-title{padding-top:50px}
.post{position:absolute;top:122px;width:280px;height:385px;background:#fff}
.post-photo{height:172px;position:relative}
.post-date{position:absolute;left:0;top:0;width:67px;height:53px;background:var(--green);color:#fff;text-align:center;font-family:"Montserrat",sans-serif}
.post-date b{display:block;font-size:18px;padding-top:6px}
.post-date span{font-size:9px}
.post-meta{height:27px;background:var(--green);color:#fff;font-size:10px;display:flex;justify-content:space-between;align-items:center;padding:0 12px}
.post h5{margin:14px 14px 8px;font:600 14px/1.4 "Montserrat",sans-serif}
.post p{margin:0 14px;font-size:10px;line-height:1.65;color:var(--muted)}
.read-more{margin:12px 14px;font:700 10px "Montserrat",sans-serif;color:var(--ink)}
.btn-load{position:absolute;left:526px;top:555px;width:150px;height:28px;border:1.5px solid var(--green);border-radius:14px;font:600 10px "Montserrat",sans-serif;display:flex;align-items:center;justify-content:center;color:var(--ink)}

/* footer */
.site-footer{height:358px;background:var(--black);color:#fff}
.footer-col{position:absolute;top:58px}
.footer-col h6{font:700 12px "Montserrat",sans-serif;margin-bottom:14px}
.footer-col li{list-style:none;font-size:10px;line-height:28px}
.footer-col li::before{content:"›";margin-right:8px}
.contact-row{display:flex;align-items:center;gap:10px;font-size:10px;margin-bottom:14px}
.contact-row.phone{font:600 17px "Montserrat",sans-serif}
.field{width:201px;height:24px;border:1px solid #444;margin-bottom:9px;font-size:10px;display:flex;align-items:center;padding-left:10px;gap:6px;color:#ccc}
.field.msg{height:67px;align-items:flex-start;padding-top:6px}
.btn-submit{width:82px;height:29px;background:var(--red);color:#fff;font:700 10px "Montserrat",sans-serif;display:flex;align-items:center;justify-content:center;margin-top:5px}
.legal{height:49px;background:var(--black);border-top:1px solid #222;color:#ccc;font-size:10px}
.legal span{position:absolute;left:160px;top:18px}
</style>
</head>
<body>

<header class="site-header">
  <div class="brand"><span class="brand-dot"></span>Zorveli Foods</div>
  <nav class="main-nav">
    <span class="active">ABOUT</span><span>PRODUCTS</span><span>SERVICES</span><span>SUPPLIERS</span><span>DOWNLOADS</span><span>NEWS</span><span>CONTACT</span>
  </nav>
  <svg class="search-icon" width="16" height="16" viewBox="0 0 16 16"><circle cx="6.5" cy="6.5" r="4.5" fill="none" stroke="#333" stroke-width="1.6"/><line x1="10" y1="10" x2="14" y2="14" stroke="#333" stroke-width="1.6"/></svg>
  <div class="btn-customer">BECOME A CUSTOMER</div>
  <div class="btn-order">ORDER ONLINE</div>
</header>

<section class="hero">
  <div class="hero-photo" role="img" aria-label="Plate of golden fried plantain slices"></div>
  <div class="hero-card">
    <div class="kicker">Welcome to</div>
    <h1>Zorveli Foods</h1>
    <p>Zorveli Foods commenced in 2004. Coming from Ghana and with a passion for cooking I realised, through school P&amp;C fundraising, that as well as enjoying my dishes,</p>
    <span class="pill-red">READ MORE</span>
  </div>
  <div class="hero-arrow" style="left:53px"><svg width="12" height="12" viewBox="0 0 12 12"><path d="M8 1 3 6l5 5" fill="none" stroke="#333" stroke-width="1.8"/></svg></div>
  <div class="hero-arrow" style="left:1109px"><svg width="12" height="12" viewBox="0 0 12 12"><path d="M4 1l5 5-5 5" fill="none" stroke="#333" stroke-width="1.8"/></svg></div>
</section>

<section class="service">
  <h2 class="service-title">WHO WE<b>SERVICE</b></h2>
  <p class="service-sub">Our beautiful freshly made food is available weekly in the following shops.</p>
  <div class="shop-tile" style="left:386px;top:62px"><div class="shop-image" role="img" aria-label="Shop photo">SHOP IMAGE</div><div class="shop-name">KOLAM PANTRY CURTIN</div></div>
  <div class="shop-tile" style="left:611px;top:62px"><div class="shop-image" role="img" aria-label="Shop photo">SHOP IMAGE</div><div class="shop-name">AINSLIE CORNER GROCER</div></div>
  <div class="shop-tile" style="left:836px;top:62px"><div class="shop-image" role="img" aria-label="Shop photo">SHOP IMAGE</div><div class="shop-name">DEAKIN FRESH MART</div></div>
  <div class="shop-tile" style="left:160px;top:341px"><div class="shop-image" role="img" aria-label="Shop photo">SHOP IMAGE</div><div class="shop-name">HARVEST TABLE,<br>BRADDON</div></div>
  <div class="shop-tile" style="left:386px;top:341px"><div class="shop-image" role="img" aria-label="Shop photo">SHOP IMAGE</div><div class="shop-name">GREENLEAF WHOLEFOODS, MAWSON</div></div>
  <div class="shop-tile" style="left:611px;top:341px"><div class="shop-image" role="img" aria-label="Shop photo">SHOP IMAGE</div><div class="shop-name">ORCHARD LANE FRUITS, BELCONNEN</div></div>
  <div class="shop-tile" style="left:836px;top:341px"><div class="shop-image" role="img" aria-label="Shop photo">SHOP IMAGE</div><div class="shop-name">LYNEHAM VILLAGE MARKET</div></div>
</section>

<section class="about">
  <h2 class="section-title">ABOUT <b>US</b></h2>
  <h3>Zorveli Foods commenced in 2004</h3>
  <p>Coming from Ghana and with a passion for cooking I realised, through school P&amp;C fundraising, that as well as enjoying my dishes, people wanted to learn more about Ghanaian food. So I started introducing pre-packaged meals at farmers' markets and food festivals to showcase Ghanaian food far and wide. They took off! People relished the exotic flavours. So why don't you give it a go?<br>Have a taste! Enjoy!</p>
</section>

<section class="casseroles">
  <h2 class="section-title">OUR CASSEROLE <b>DISHES</b></h2>
  <div class="dish" style="left:160px"><div class="dish-photo" role="img" aria-label="Chicken and spinach casserole slice on a plate" style="background:linear-gradient(160deg,#8a3a22 0%,#e6d38a 45%,#f4ecd2 75%,#3b5a8a 100%)"></div><h4>CHICKEN AND SPINACH<br>CASSEROLE</h4></div>
  <div class="dish" style="left:460px"><div class="dish-photo" role="img" aria-label="Spicy beef casserole in a clay pot" style="background:radial-gradient(ellipse at 50% 55%,#5a2a16 0%,#8b4a25 40%,#d9cfc2 85%)"></div><h4>SPICY BEEF CASSEROLE</h4></div>
  <div class="dish" style="left:760px"><div class="dish-photo" role="img" aria-label="Black-eyed beans casserole with vegetables" style="background:radial-gradient(ellipse at 50% 50%,#b9562a 0%,#8a3f1d 45%,#d9a066 85%)"></div><h4>BLACK-EYED BEANS<br>CASSEROLE</h4></div>
</section>

<section class="catering">
  <p>We also cater for functions, either cocktail or sit-down dining, where we offer special dishes such as jollof rice, gari fortor, etc.</p>
  <div class="btn-outline-light">CONTACT US NOW</div>
</section>

<section class="offer">
  <h2 class="section-title">WE ALSO <b>OFFER</b></h2>
  <div class="offer-card" style="left:160px"><div class="offer-photo" role="img" aria-label="Bowl of black-eyed bean salad" style="background:radial-gradient(ellipse at 45% 55%,#8a5a3a 0%,#b88a5a 35%,#e8e2da 80%)"></div><div class="offer-label">Black-eyed beans snacks served with our home made sweet chilli sauce or traditional</div></div>
  <div class="offer-card" style="left:612px"><div class="offer-photo" role="img" aria-label="Squares of coconut sweet on a plate" style="background:radial-gradient(ellipse at 55% 50%,#d8c48a 0%,#c9b178 40%,#b07a55 90%)"></div><div class="offer-label">Coconut sweet.</div></div>
</section>

<section class="blog">
  <h2 class="section-title">OUR <b>BLOG</b></h2>
  <article class="post" style="left:160px">
    <div class="post-photo" role="img" aria-label="Red casserole pot on a kitchen bench" style="background:linear-gradient(150deg,#c9c2b8 0%,#c23a1e 45%,#8a2412 80%)"><div class="post-date"><b>11</b><span>Oct, 2019</span></div></div>
    <div class="post-meta"><span>By Admin</span><span>Comments</span></div>
    <h5>Lorem ipsum dolor sit amet, consectetur adipiscing elit, sed do</h5>
    <p>Nemo enim ipsam voluptatem quia voluptas sit aspernatur aut odit aut fugit, sed quia consequuntur magni dolores eos qui ratione voluptatem sequi nesciunt.</p>
    <div class="read-more">READ MORE ›</div>
  </article>
  <article class="post" style="left:460px">
    <div class="post-photo" role="img" aria-label="Jar of red chilli sauce on a wooden table" style="background:linear-gradient(150deg,#b8a692 0%,#d8472a 45%,#7a4a2e 85%)"><div class="post-date"><b>7</b><span>Oct, 2019</span></div></div>
    <div class="post-meta"><span>By Admin</span><span>Comments</span></div>
    <h5>Lorem ipsum dolor sit amet, consectetur adipiscing elit, sed do</h5>
    <p>Nemo enim ipsam voluptatem quia voluptas sit aspernatur aut odit aut fugit, sed quia consequuntur magni dolores eos qui ratione voluptatem sequi nesciunt.</p>
    <div class="read-more">READ MORE ›</div>
  </article>
  <article class="post" style="left:760px">
    <div class="post-photo" role="img" aria-label="Baked dish held in oven-mitted hands" style="background:linear-gradient(160deg,#9a948c 0%,#d8b87a 50%,#6a5a4a 100%)"><div class="post-date"><b>11</b><span>Oct, 2019</span></div></div>
    <div class="post-meta"><span>By Admin</span><span>Comments</span></div>
    <h5>Lorem ipsum dolor sit amet, consectetur adipiscing elit, sed do</h5>
    <p>Nemo enim ipsam voluptatem quia voluptas sit aspernatur aut odit aut fugit, sed quia consequuntur magni dolores eos qui ratione voluptatem sequi nesciunt.</p>
    <div class="read-more">READ MORE ›</div>
  </article>
  <div class="btn-load">LOAD MORE POST</div>
</section>

<footer class="site-footer">
  <div class="footer-col" style="left:160px">
    <h6>QUICK LINKS</h6>
    <ul><li>About</li><li>Products</li><li>Services</li><li>Suppliers</li><li>Downloads</li><li>News</li><li>Contact</li></ul>
  </div>
  <div class="footer-col" style="left:385px">
    <h6>SHOP WE SERVED</h6>
    <ul><li>Kolam Pantry Curtin</li><li>Ainslie Corner Grocer</li><li>Deakin Fresh Mart</li><li>Harvest Table, Braddon</li><li>Greenleaf Wholefoods, Mawson</li><li>Orchard Lane Fruits, Belconnen</li><li>Lyneham Village Market</li></ul>
  </div>
  <div class="footer-col" style="left:610px">
    <h6>GET IN TOUCH</h6>
    <div class="contact-row"><svg width="12" height="14" viewBox="0 0 12 14"><path d="M6 13S1 8 1 5a5 5 0 0 1 10 0c0 3-5 8-5 8z" fill="#fff"/><circle cx="6" cy="5" r="1.8" fill="#000"/></svg><span>14 Mallee Street, Canberra<br>ACT 2601, Australia</span></div>
    <div class="contact-row"><svg width="14" height="10" viewBox="0 0 14 10"><rect x="0.5" y="0.5" width="13" height="9" fill="none" stroke="#fff"/><path d="M.5.5 7 6l6.5-5.5" fill="none" stroke="#fff"/></svg><span>hello@zorvelifoods.com.au</span></div>
    <div class="contact-row phone"><svg width="14" height="14" viewBox="0 0 14 14"><path d="M3 1l2 3-1.5 1.5a8 8 0 0 0 5 5L10 9l3 2-1.5 2.5C6 13 1 8 .5 2.5z" fill="#fff"/></svg><span>02 6100 4821</span></div>
    <div class="contact-row"><svg width="14" height="14" viewBox="0 0 14 14"><circle cx="7" cy="7" r="6" fill="none" stroke="#fff"/><path d="M1 7h12M7 1c-3 3-3 9 0 12M7 1c3 3 3 9 0 12" fill="none" stroke="#fff"/></svg><span>www.zorvelifoods.com.au</span></div>
  </div>
  <div class="footer-col" style="left:836px">
    <h6>SEND US A MESSAGE</h6>
    <div class="field">Your Name</div>
    <div class="field">Your Email</div>
    <div class="field">Subject</div>
    <div class="field msg">Message</div>
    <div class="btn-submit">SUBMIT</div>
  </div>
</footer>
<div class="legal" style="position:relative"><span>© 2019 Zorveli Foods | All rights reserved.</span></div>

</body>
</html>
```